Solar Advertising Flier to generate Biz

I need a advertisement that generates business to be used in a mailer for marketing purposes.

Im attaching a file that is a an idea of advertisement.
I do not want the "ZVN" specific information on it.
I want the background solar panels.
Same information as the ad.
And I've attached my Logo - I want the color scheme to match this.

Thank you

Target Market(s)

Middle to Upper Class Home Owners

Industry/Entity Type

Solar Energy

Requirements
Must have
• A call to action
• A professional look
Nice to have
• A family
• Great looking solar panels
Should not have
• Cartoons

```html
<!DOCTYPE html>
<html lang="en">
<head>
<meta charset="utf-8">
<title>Go Solar – Bright Path Energy</title>
<link rel="stylesheet" href="https://fonts.googleapis.com/css2?family=Roboto+Condensed:wght@400;700&family=Source+Sans+3:wght@400;600;700&family=Oswald:wght@500;700&display=swap">
<style>
  :root{
    --blue:#1e95d3;
    --blue-deep:#1570b8;
    --green:#9ccc2e;
    --ink:#333a40;
    --grey:#8a8d90;
    --grey-band:#ececec;
    --yellow:#ffe43a;
    --sky-top:#cfe6f7;
    --sky-low:#f3f9fd;
    --panel-dark:#2b3f8f;
    --panel-mid:#5c7cc4;
  }
  *{margin:0;padding:0;box-sizing:border-box}
  html,body{width:998px;height:1200px;overflow:hidden;background:#fff}
  .flier{position:relative;width:998px;height:1200px;overflow:hidden;background:#fff;font-family:"Source Sans 3",Arial,sans-serif;color:var(--ink)}
  .art{position:absolute;left:0;top:0}
  .brand{position:absolute;left:560px;top:62px;width:300px;display:flex;flex-direction:column;align-items:center;gap:10px}
  .brand-dot{width:74px;height:74px;border-radius:50%;background:var(--blue)}
  .brand-name{font-weight:600;font-size:26px;letter-spacing:.5px;color:var(--blue-deep)}
  .headline{position:absolute;left:112px;top:688px;font-family:"Roboto Condensed",Arial,sans-serif;font-weight:700;font-size:118px;line-height:1;color:var(--blue);letter-spacing:1px;text-shadow:3px 3px 0 var(--green)}
  .subhead{position:absolute;left:120px;top:808px;font-family:"Roboto Condensed",Arial,sans-serif;font-weight:700;font-size:25px;color:var(--ink)}
  .benefits{position:absolute;left:60px;top:852px;width:620px;list-style:none}
  .benefit-row{display:flex;gap:36px;align-items:center;height:42px;padding-left:50px;background:linear-gradient(90deg,#fff 0%,var(--grey-band) 35%,var(--grey-band) 85%,#fff 100%);margin-bottom:4px;font-size:18px}
  .benefit-row:nth-child(even){background:linear-gradient(90deg,#fff 0%,#f6f6f6 50%,#fff 100%)}
  .benefit{display:flex;align-items:center;gap:10px}
  .benefit strong{font-weight:700}
  .tick{width:20px;height:20px;flex:none}
  .how{position:absolute;left:128px;top:994px;width:540px}
  .how h2{font-size:18px;font-weight:700;color:var(--blue);margin-bottom:4px}
  .how p{font-size:13px;line-height:1.35;color:var(--ink)}
  .how strong{font-weight:700}
  .contact{position:absolute;left:128px;top:1086px;display:flex;align-items:center;gap:20px}
  .call{color:var(--blue)}
  .call-line{display:flex;align-items:center;gap:8px;font-weight:700;font-size:18px}
  .call-number{font-family:"Roboto Condensed",Arial,sans-serif;font-size:26px;font-weight:700}
  .call-sub{font-size:18px}
  .divider{width:1px;height:54px;background:#c8c8c8}
  .details{font-size:14px;color:var(--ink);line-height:1.6}
  .detail{display:flex;align-items:center;gap:8px}
  .web{letter-spacing:2.5px}
  .rebate{position:absolute;left:683px;top:840px;width:240px;height:240px;border-radius:50%;background:var(--blue);border:5px solid var(--yellow);box-shadow:0 6px 14px rgba(0,0,0,.25);display:flex;flex-direction:column;align-items:center;justify-content:center;font-family:"Oswald",Arial,sans-serif;color:var(--yellow);text-align:center;line-height:1.1}
  .rebate-small{font-size:24px;font-weight:500}
  .rebate-big{font-size:76px;font-weight:700;line-height:1}
</style>
</head>
<body>
<div class="flier">
  <svg class="art" width="998" height="1200" viewBox="0 0 998 1200">
    <defs>
      <linearGradient id="sky" x1="0" y1="0" x2="0" y2="1">
        <stop offset="0" stop-color="var(--sky-top)"/>
        <stop offset="1" stop-color="var(--sky-low)"/>
      </linearGradient>
      <linearGradient id="roof" x1="0" y1="0" x2="0.3" y2="1">
        <stop offset="0" stop-color="#8fb5e6"/>
        <stop offset=".45" stop-color="var(--panel-mid)"/>
        <stop offset=".8" stop-color="var(--panel-dark)"/>
        <stop offset="1" stop-color="#dfe8f2"/>
      </linearGradient>
      <linearGradient id="install" x1="0" y1="0" x2="1" y2="1">
        <stop offset="0" stop-color="#4d86d6"/>
        <stop offset="1" stop-color="#243d8a"/>
      </linearGradient>
      <linearGradient id="house" x1="0" y1="0" x2="0" y2="1">
        <stop offset="0" stop-color="#6d9be0"/>
        <stop offset=".55" stop-color="#8c8f96"/>
        <stop offset="1" stop-color="#c9c6c0"/>
      </linearGradient>
    </defs>

    <rect class="sky-band" x="0" y="0" width="998" height="680" fill="url(#sky)"/>
    <polygon class="corner-panel" points="998,650 998,1150 790,1150 930,720" fill="var(--grey)"/>

    <path class="hero-photo" role="img" aria-label="Smiling installer in hard hat and safety vest crouching on a roof in front of rows of solar panels under a blue sky"
      d="M0 250 C200 170 430 230 620 300 C760 350 900 330 998 270 L998 540 C780 630 480 670 0 620 Z" fill="url(#roof)"/>

    <path class="wave-blue-top" d="M0 240 C180 160 420 200 620 280 C760 335 900 320 998 250 L998 268 C900 335 760 352 620 300 C430 230 200 180 0 262 Z" fill="var(--blue)"/>
    <path class="wave-green-top" d="M0 150 C250 70 470 160 640 235 C780 295 900 270 998 200 L998 225 C900 300 780 320 640 262 C470 190 250 110 0 180 Z" fill="var(--green)"/>
    <path class="wave-blue-bottom" d="M0 620 C480 670 780 630 998 540 L998 565 C780 655 480 692 0 642 Z" fill="var(--blue)"/>
    <path class="wave-green-bottom" d="M0 648 C480 698 780 662 998 572 L998 620 C780 695 480 722 0 670 Z" fill="var(--green)"/>

    <circle class="photo-ring" cx="786" cy="545" r="130" fill="var(--green)"/>
    <circle class="install-photo" role="img" aria-label="Worker in harness and blue hard hat fixing a solar panel onto a roof" cx="786" cy="545" r="120" fill="url(#install)"/>
    <circle class="photo-ring" cx="822" cy="770" r="122" fill="var(--green)"/>
    <circle class="house-photo" role="img" aria-label="Two-storey family home with solar panels on the roof and bare trees behind" cx="822" cy="770" r="112" fill="url(#house)"/>
  </svg>

  <div class="brand">
    <span class="brand-dot"></span>
    <span class="brand-name">BRIGHT PATH ENERGY</span>
  </div>

  <h1 class="headline">GO SOLAR</h1>
  <p class="subhead">Get Grandfathered before the New Utility Rate Deadline</p>

  <ul class="benefits">
    <li class="benefit-row">
      <span class="benefit"><svg class="tick" viewBox="0 0 20 20"><circle cx="10" cy="10" r="8.5" fill="none" stroke="var(--blue)" stroke-width="2"/><path d="M5.5 10.5l3 3 6-6.5" fill="none" stroke="var(--blue)" stroke-width="2.4" stroke-linecap="round" stroke-linejoin="round"/></svg><span><strong>$0 Down,</strong> no upfront cost.</span></span>
      <span class="benefit"><svg class="tick" viewBox="0 0 20 20"><circle cx="10" cy="10" r="8.5" fill="none" stroke="var(--blue)" stroke-width="2"/><path d="M5.5 10.5l3 3 6-6.5" fill="none" stroke="var(--blue)" stroke-width="2.4" stroke-linecap="round" stroke-linejoin="round"/></svg><span><strong>Save 95% off</strong> your utility bill.</span></span>
    </li>
    <li class="benefit-row">
      <span class="benefit"><svg class="tick" viewBox="0 0 20 20"><circle cx="10" cy="10" r="8.5" fill="none" stroke="var(--blue)" stroke-width="2"/><path d="M5.5 10.5l3 3 6-6.5" fill="none" stroke="var(--blue)" stroke-width="2.4" stroke-linecap="round" stroke-linejoin="round"/></svg><span><strong>Protect yourself</strong> from rising energy costs</span></span>
    </li>
    <li class="benefit-row">
      <span class="benefit"><svg class="tick" viewBox="0 0 20 20"><circle cx="10" cy="10" r="8.5" fill="none" stroke="var(--blue)" stroke-width="2"/><path d="M5.5 10.5l3 3 6-6.5" fill="none" stroke="var(--blue)" stroke-width="2.4" stroke-linecap="round" stroke-linejoin="round"/></svg><span>Provide clean, reliable energy for your family <strong>powered by the sun.</strong></span></span>
    </li>
  </ul>

  <section class="how">
    <h2>How it works...</h2>
    <p>Your solar system allows you to <strong>generate your own clean power</strong> and COSTS LESS than your current utility company. Simply pay by the month, like you do now...but at a LOWER rate and <strong>START SAVING IMMEDIATELY.</strong></p>
  </section>

  <div class="contact">
    <div class="call">
      <div class="call-line">Call Today
        <svg width="20" height="20" viewBox="0 0 24 24"><path d="M6.6 10.8a15.1 15.1 0 0 0 6.6 6.6l2.2-2.2a1 1 0 0 1 1-.25 11.4 11.4 0 0 0 3.6.57 1 1 0 0 1 1 1V20a1 1 0 0 1-1 1A17 17 0 0 1 3 4a1 1 0 0 1 1-1h3.5a1 1 0 0 1 1 1c0 1.25.2 2.45.57 3.57a1 1 0 0 1-.25 1z" fill="var(--green)"/></svg>
        <span class="call-number">555-014-2287</span>
      </div>
      <div class="call-sub">For A No Obligation Consultation</div>
    </div>
    <span class="divider"></span>
    <div class="details">
      <div class="detail"><svg width="16" height="16" viewBox="0 0 24 24"><path d="M12 3 2 12h3v8h5v-5h4v5h5v-8h3z" fill="var(--green)"/></svg>4180 W Canyon Ridge Rd B-210 Mesa AZ 85201</div>
      <div class="detail web"><svg width="16" height="16" viewBox="0 0 24 24"><circle cx="12" cy="12" r="9" fill="none" stroke="var(--green)" stroke-width="2"/><path d="M3 12h18M12 3c3 3.5 3 14.5 0 18M12 3c-3 3.5-3 14.5 0 18" fill="none" stroke="var(--green)" stroke-width="1.6"/></svg>www.ClearSkySolarCo.com</div>
    </div>
  </div>

  <div class="rebate">
    <span class="rebate-small">CALL TODAY</span>
    <span class="rebate-small">AND RECEIVE A</span>
    <span class="rebate-big">$500</span>
    <span class="rebate-small">CASH REBATE</span>
  </div>

  <svg class="art" width="998" height="1200" viewBox="0 0 998 1200" aria-hidden="true">
    <rect class="footer-rule" x="0" y="1150" width="998" height="6" fill="var(--blue)"/>
    <rect class="footer-rule" x="0" y="1158" width="998" height="10" fill="var(--grey)"/>
  </svg>
</div>
</body>
</html>
```